Paws and Meadows is a dog walking service that offers home boarding and pet taxi

I am looking for a eye catching A5 leaflet/flyer design for my dog walking business Paws and Meadows.

The flyer must have my company logo on it (jpeg), a picture of my van (jpeg) and a picture of dogs playing (jpegs 1-5).

The fonts must be easy to read. I am not set on any colour scheme but do like the idea of having a natural background. IE. Green grass and blue sky or some forest setting with green trees. If you don't like this idea or its hard to work with don't worry I am open minded so be creative and do what you thinks best.

I'll provide quick feedback to designs that i like and so we can work together.

The flyers must contain the following:

60 minute group and individual walks
GPS Tracked Walks
Home Boarding
Pet Taxi
Puppy/Pet visits

Offer: 50% off first weeks dogs walks with this flyer.

As well as containing my contact info:

07915382046
www.paws-and-meadows.co.uk
paws-and-meadows@mailbrook.co.uk

Chatterbook, Chirpline and Snapgallery logos must be present as well.

Thanks and Good luck!

Target Market(s)

ANYONE WHO NEEDS THEIR DOG WALKED OR LOOKED AFTER WHEN THEY ARE ON HOLIDAY

Industry/Entity Type

Business

Contact Information for Business Card

THE BUSINESS CARD MUST DISPLAY THE LOGO THAT HAS BEEN UPLOADED IN A FILE. IT MUST LOOK SHARP AND PROFESSIONAL. CONTAIN ALL CONTACT INFO AND HAVE SERVICES OFFERED. SEE PROJECT DESCRIPTION FOR FLYER.

Font styles to use
Serif
Sans Serif

Requirements
Must have
• SEE PROJECT DESCRIPTION
Nice to have
• IT WOULD BE NICE TO HAVE PHOTOS OF MY VAN AND DOGS PLAYING. I HAVE UPLOADED SOME PICS OF VAN TO BE USED AND THERE ARE PICS OF DOGS PLAYING THAT COULD BE USED.

```html
<!DOCTYPE html>
<html lang="en">
<head>
<meta charset="utf-8">
<title>Paws and Meadows – Dog Walking Flyer</title>
<link rel="stylesheet" href="https://fonts.googleapis.com/css2?family=Lilita+One&family=Lato:wght@400;700&family=Rubik:wght@700;800&display=swap">
<style>
  :root {
    --page-bg: #e6e6e6;
    --grass-dark: #2f7d1e;
    --grass-mid: #4fa52c;
    --grass-light: #74c23d;
    --band-purple: #8e4f9c;
    --band-blue: #1670b8;
    --headline-blue: #1a6fc4;
    --fun-purple: #7e4aa4;
    --service-purple: #9a4fa3;
    --ribbon-red: #d72b20;
    --contact-red: #d3241b;
    --offer-blue: #1a6cb8;
    --white: #ffffff;
  }
  * { box-sizing: border-box; margin: 0; padding: 0; }
  html, body {
    width: 1200px; height: 927px; overflow: hidden;
    background: var(--page-bg);
  }
  .flyer {
    position: absolute; left: 20px; top: 53px;
    width: 1160px; height: 820px; overflow: hidden;
    background: var(--grass-mid);
  }
  .grass {
    position: absolute; inset: 0;
    background:
      radial-gradient(ellipse at 30% 40%, var(--grass-light) 0%, transparent 55%),
      radial-gradient(ellipse at 80% 70%, var(--grass-light) 0%, transparent 50%),
      linear-gradient(160deg, var(--grass-mid), var(--grass-dark));
  }
  .band-top { position: absolute; left: 0; top: 0; width: 100%; height: 23px; background: var(--band-purple); }
  .band-bottom { position: absolute; left: 0; bottom: 0; width: 100%; height: 26px; background: var(--band-blue); }

  .offer {
    position: absolute; left: 960px; top: 0; width: 168px; height: 159px;
    filter: drop-shadow(0 3px 4px rgba(0,0,0,.35));
    z-index: 4;
  }
  .offer svg { position: absolute; inset: 0; }
  .offer-text {
    position: relative; text-align: center; color: var(--white);
    font-family: "Rubik", sans-serif; font-weight: 800; padding-top: 34px;
  }
  .offer-big { font-size: 28px; line-height: 1; }
  .offer-small { font-size: 14px; line-height: 1.15; margin-top: 4px; letter-spacing: .3px; }

  .headline {
    position: absolute; left: 215px; top: 40px; width: 340px;
    text-align: center; transform: rotate(-2deg);
    font-family: "Lilita One", sans-serif; font-weight: 400; font-size: 47px; line-height: 48px;
    color: var(--headline-blue); letter-spacing: .5px;
    -webkit-text-stroke: 2px var(--white); paint-order: stroke fill;
    text-shadow: 0 0 3px var(--white), 2px 3px 3px rgba(0,0,0,.35);
    z-index: 5;
  }
  .headline .line-2 { display: block; margin-left: -20px; }

  .polaroid {
    position: absolute; background: var(--white);
    padding: 16px 16px 62px;
    box-shadow: 3px 6px 12px rgba(0,0,0,.4);
  }
  .polaroid .photo { width: 100%; height: 100%; }
  .polaroid-van { left: 135px; top: 178px; width: 310px; height: 290px; transform: rotate(8deg); z-index: 1; }
  .polaroid-van .photo { background: linear-gradient(180deg, #6aa7e0 0%, #a9cbe6 35%, #4f8a3b 60%, #3b5a32 100%); }
  .polaroid-park { left: 450px; top: 140px; width: 295px; height: 285px; transform: rotate(-8deg); z-index: 2; }
  .polaroid-park .photo { background: linear-gradient(180deg, #c9dfee 0%, #3f7a2e 20%, #78c437 45%, #64b12b 100%); }
  .polaroid-water { left: 752px; top: 190px; width: 272px; height: 275px; transform: rotate(3deg); z-index: 1; }
  .polaroid-water .photo { background: linear-gradient(180deg, #d8d6d0 0%, #8a8a7e 35%, #6e6a60 60%, #4b4a44 100%); }

  .tagline {
    position: absolute; left: 376px; top: 447px; width: 400px;
    text-align: center; font-family: "Lilita One", sans-serif;
    font-size: 30px; line-height: 38px; letter-spacing: .5px;
    -webkit-text-stroke: 2px var(--white); paint-order: stroke fill;
    text-shadow: 0 0 3px var(--white), 1px 2px 2px rgba(0,0,0,.3);
    z-index: 5;
  }
  .tagline .tag-1 { color: var(--headline-blue); display: block; }
  .tagline .tag-2 { color: var(--fun-purple); display: block; }

  .services {
    position: absolute; left: 478px; top: 528px; width: 240px; height: 232px;
    background: var(--service-purple); border: 2px solid var(--white);
    transform: rotate(-4deg); padding: 14px 8px 0 14px;
    box-shadow: 2px 3px 6px rgba(0,0,0,.3);
  }
  .services ul { list-style: none; }
  .services li {
    position: relative; color: var(--white);
    font-family: "Lato", sans-serif; font-size: 22px; line-height: 26px;
    margin-bottom: 7px;
  }
  .services li::before {
    content: ""; position: absolute; left: -41px; top: 4px;
    width: 20px; height: 20px; border-radius: 50%;
    background: var(--service-purple); border: 2px solid var(--white);
  }

  .contact { position: absolute; left: 53px; top: 588px; width: 296px; }
  .contact-ribbon {
    position: relative; height: 30px; background: var(--ribbon-red);
    color: var(--white); text-align: center;
    font-family: "Rubik", sans-serif; font-weight: 700; font-size: 21px; line-height: 30px;
    clip-path: polygon(0 0, 100% 0, 96% 50%, 100% 100%, 0 100%, 4% 50%);
  }
  .contact-panel {
    height: 176px; background: rgba(240,244,236,.86);
    text-align: center; color: var(--contact-red);
    font-family: "Lato", sans-serif; font-size: 19px; line-height: 28px;
    padding-top: 26px;
  }
  .contact-panel .email { font-size: 17px; }

  .brand-card {
    position: absolute; left: 876px; top: 572px; width: 212px; height: 190px;
    background: var(--white); transform: rotate(8deg);
    box-shadow: 3px 6px 12px rgba(0,0,0,.4);
    text-align: center; padding-top: 26px;
    font-family: "Lato", sans-serif;
  }
  .brand-mark { width: 22px; height: 22px; border-radius: 50%; background: #e8a21c; margin: 0 auto 8px; }
  .brand-name { font-weight: 700; font-size: 21px; color: #2b2b2b; }
  .social { list-style: none; margin-top: 12px; display: flex; flex-direction: column; align-items: center; gap: 3px; }
  .social li { font-size: 13px; font-weight: 700; color: var(--contact-red); display: flex; align-items: center; gap: 5px; line-height: 16px; }
  .social li::before { content: ""; width: 10px; height: 10px; background: var(--contact-red); }
</style>
</head>
<body>
  <main class="flyer">
    <div class="grass" role="img" aria-label="Close-up of lush green lawn grass"></div>
    <div class="band-top"></div>
    <div class="band-bottom"></div>

    <aside class="offer">
      <svg width="168" height="159" viewBox="0 0 168 159" aria-hidden="true">
        <polygon points="0,0 168,0 168,159 84,132 0,159" fill="var(--offer-blue)" stroke="#ffffff" stroke-width="3"/>
      </svg>
      <div class="offer-text">
        <div class="offer-big">50 % OFF</div>
        <div class="offer-small">FIRST WEEKS<br>DOGS WALKS<br>WITH THIS FLYER.</div>
      </div>
    </aside>

    <div class="polaroid polaroid-van">
      <div class="photo" role="img" aria-label="Photo of the company van parked on a sunny track"></div>
    </div>
    <div class="polaroid polaroid-park">
      <div class="photo" role="img" aria-label="Photo of several dogs playing together on a park field"></div>
    </div>
    <div class="polaroid polaroid-water">
      <div class="photo" role="img" aria-label="Photo of dogs running through shallow water"></div>
    </div>

    <h1 class="headline">WE'D LOVE <span class="line-2">TO TAKE CARE</span>OF YOUR PET</h1>

    <p class="tagline"><span class="tag-1">IT WILL GONNA HAVE</span><span class="tag-2">SO MUCH FUN</span></p>

    <section class="services">
      <ul>
        <li>60 minute group<br>and individual<br>walks</li>
        <li>GPS Tracked Walks</li>
        <li>Home Boarding</li>
        <li>Pet Taxi</li>
        <li>Puppy/Pet visits</li>
      </ul>
    </section>

    <section class="contact">
      <div class="contact-ribbon">CONTACT US</div>
      <div class="contact-panel">
        <div>07915382046</div>
        <div>www.paws-and-meadows.co.uk</div>
        <div class="email">paws-and-meadows@mailbrook.co.uk</div>
      </div>
    </section>

    <div class="brand-card">
      <div class="brand-mark"></div>
      <div class="brand-name">Paws and Meadows</div>
      <ul class="social">
        <li>Chatterbook</li>
        <li>Chirpline</li>
        <li>Snapgallery</li>
      </ul>
    </div>
  </main>
</body>
</html>
```